Business Card Design - Cryotherapy

We need a custom created business card for our company FrostLeaf Spa. We provide whole body cryotherapy and localized cryotherapy to our clients. Please be creative.
Please see our website for idea's on design.
www.frostleafspa-example.com
Industry/Entity Type
Business
Contact Information for Business Card
Name, Position, Phone Number, Address, Website, Email
Look and feel
Each slider illustrates characteristics of the customer's brand and the style your logo design should communicate.

```html
<!DOCTYPE html>
<html lang="en">
<head>
<meta charset="utf-8">
<title>FrostLeaf Spa Business Card</title>
<link href="https://fonts.googleapis.com/css2?family=Questrial&family=Arimo:wght@400;700&display=swap" rel="stylesheet">
<style>
  :root {
    --page: #e9e7e3;
    --paper: #ffffff;
    --charcoal: #232425;
    --teal: #1fa3b8;
    --green: #1f8a4c;
    --grey-text: #c9cbcc;
    --divider: #8a8c8e;
  }
  html, body {
    margin: 0;
    padding: 0;
    width: 1200px;
    height: 902px;
    overflow: hidden;
    background: var(--page);
  }
  .canvas {
    position: relative;
    width: 1200px;
    height: 902px;
    display: flex;
    flex-direction: column;
    align-items: center;
    justify-content: center;
    gap: 36px;
  }
  .card {
    position: relative;
    width: 700px;
    height: 400px;
    background: var(--paper);
    box-shadow: 0 4px 14px rgba(0,0,0,0.18);
    overflow: hidden;
  }
  .card-shape {
    position: absolute;
    inset: 0;
  }
  .brand {
    position: absolute;
    left: 70px;
    top: 48px;
    display: flex;
    align-items: center;
    gap: 14px;
    font-family: "Questrial", sans-serif;
    font-size: 46px;
    color: var(--green);
    letter-spacing: 1px;
  }
  .brand-dot {
    width: 44px;
    height: 44px;
    border-radius: 50%;
    background: var(--teal);
  }
  .holder {
    position: absolute;
    left: 40px;
    top: 300px;
    font-family: "Arimo", sans-serif;
  }
  .holder-name {
    font-size: 26px;
    font-weight: 700;
    color: var(--teal);
    margin: 0;
  }
  .holder-role {
    font-size: 21px;
    color: var(--grey-text);
    margin: 4px 0 0;
  }
  .divider {
    position: absolute;
    left: 352px;
    top: 232px;
    width: 1px;
    height: 140px;
    background: var(--divider);
  }
  .contact-list {
    position: absolute;
    left: 374px;
    top: 224px;
    margin: 0;
    padding: 0;
    list-style: none;
    font-family: "Questrial", sans-serif;
    font-size: 15px;
    color: var(--grey-text);
    line-height: 27px;
  }
  .contact-list li {
    display: flex;
    align-items: flex-start;
    gap: 12px;
  }
  .contact-icon {
    flex: none;
    width: 13px;
    height: 13px;
    margin-top: 7px;
  }
  .contact-indent {
    padding-left: 25px;
  }
  .back-brand {
    position: absolute;
    inset: 0;
    display: flex;
    align-items: center;
    justify-content: center;
    gap: 18px;
    font-family: "Questrial", sans-serif;
    font-size: 58px;
    color: var(--teal);
  }
  .back-brand .brand-dot {
    width: 56px;
    height: 56px;
  }
</style>
</head>
<body>
<main class="canvas">
  <section class="card card-front">
    <svg class="card-shape" viewBox="0 0 700 400" width="700" height="400">
      <path d="M0,200 C150,250 330,240 700,30" fill="none" stroke="var(--teal)" stroke-width="5"/>
      <path d="M0,210 C150,260 330,250 700,40 L700,400 L0,400 Z" fill="var(--charcoal)"/>
    </svg>
    <div class="brand"><span class="brand-dot"></span>FrostLeaf Spa</div>
    <div class="holder">
      <p class="holder-name">Ellen's Apothecary</p>
      <p class="holder-role">Owner</p>
    </div>
    <div class="divider"></div>
    <ul class="contact-list">
      <li>
        <svg class="contact-icon" viewBox="0 0 13 13"><rect width="13" height="13" rx="2" fill="var(--teal)"/><path d="M4,3 L5.5,3 L6,5 L5,6 C5.6,7.2 6.2,7.8 7,8 L8,7 L10,7.5 L10,9 C7,10 3,6 4,3Z" fill="var(--charcoal)"/></svg>
        <span>(555) 014-2290</span>
      </li>
      <li>
        <svg class="contact-icon" viewBox="0 0 13 13"><rect width="13" height="13" rx="2" fill="var(--teal)"/><rect x="3" y="4" width="7" height="5" fill="none" stroke="var(--charcoal)" stroke-width="1"/><path d="M3,4 L6.5,7 L10,4" fill="none" stroke="var(--charcoal)" stroke-width="1"/></svg>
        <span>info@frostleafspa-example.com</span>
      </li>
      <li>
        <svg class="contact-icon" viewBox="0 0 13 13"><rect width="13" height="13" rx="2" fill="var(--teal)"/><circle cx="6.5" cy="6.5" r="3.3" fill="none" stroke="var(--charcoal)" stroke-width="1"/><path d="M3.2,6.5 H9.8 M6.5,3.2 V9.8" stroke="var(--charcoal)" stroke-width="0.8"/></svg>
        <span>http://frostleafspa-example.com</span>
      </li>
      <li>
        <svg class="contact-icon" viewBox="0 0 13 13"><rect width="13" height="13" rx="2" fill="var(--teal)"/><path d="M6.5,10.5 C4.5,8 4,7 4,5.5 A2.5,2.5 0 0 1 9,5.5 C9,7 8.5,8 6.5,10.5Z" fill="var(--charcoal)"/></svg>
        <span>420 Birch Hollow Lane</span>
      </li>
      <li class="contact-indent">Suite 12 Maplewood, IL 60000</li>
    </ul>
  </section>

  <section class="card card-back">
    <div class="back-brand"><span class="brand-dot"></span>FrostLeaf Spa</div>
  </section>
</main>
</body>
</html>
```